Review/Re-Design Supermarket E-Commerce website

We have launched our Supermarket E-commerce Website but feel it is lacking a modern feel.

Please re-design the current Supermarket E-commerce site, creating a more modern look and feel.

I am looking for design changes to things such as:

- Fonts
- Button shape & Size
- Shapes of boxes
- Layout of drop down menus
- A new shopping cart / button
- The Header (and in particular the use and positioning of the logo)
- Supplying a generic background image (currently berries)

Please do not change the structure of the page. For instance, the category selection will always be on the left, the items will always be displayed in rows of 3 and the shopping cart should be on the right.
Updates

Current site can be found at www.brovanmarket.com.au

Project Deadline Extended
Reason: designs coming in are generally too different from current design. we are looking for less that 10% change to the overall look and feel. one aspect that needs a lot of work is the checkout cart on the right hand side. please checkout http://www2.pelkinfreshmart.com.au/?gclid=QXRP4kdmwnLBHTYEzJuaPGEKtB

Target Market(s)

Consumers buying their weekly grocery shopping online

Industry/Entity Type

Shopping

Number of Pages Required

1 page

Requirements
Must have
• Stick to the branding of the Logo. Which is Red, Blue and White.
• Other colours may be used in small percentages.
Should not have
• Do not change the Structure of the site.

```html
<!DOCTYPE html>
<html lang="en">
<head>
<meta charset="utf-8">
<title>Brovan Market – Fruit</title>
<link href="https://fonts.googleapis.com/css2?family=Arimo:wght@400;700&display=swap" rel="stylesheet">
<style>
:root{
  --blue:#1565b4;
  --navy:#1b4f9c;
  --red:#e8202a;
  --green:#8cc63f;
  --text:#444;
  --muted:#999;
  --faint:#ccc;
  --line:#e3e3e3;
  --bar:#f4f4f4;
  --foot:#f6f6f6;
  --white:#fff;
}
*{box-sizing:border-box;margin:0;padding:0}
html,body{width:1200px;height:1199px;overflow:hidden}
body{font-family:"Arimo",Arial,sans-serif;color:var(--text);background:var(--white);position:relative;font-size:9px}
.abs{position:absolute}
.scene-left{left:0;top:0;width:210px;height:580px;background:linear-gradient(180deg,#f3efe8 0%,#e7b78a 28%,#d9853f 45%,#f1e4d2 62%,#e9c9a8 80%,#f7f5f2 100%)}
.scene-right{left:990px;top:0;width:210px;height:600px;background:linear-gradient(180deg,#eef0ea 0%,#b9cf8c 15%,#f5f2f0 28%,#d9495a 40%,#e7b77b 55%,#f4f0ee 65%,#c9a6b6 80%,#f7f7f7 100%)}
.page{left:210px;top:0;width:780px;height:1199px;background:var(--white)}
.topbar{left:210px;top:0;width:780px;height:27px;background:var(--bar);font-size:10px}
.topbar .phone{left:23px;top:9px;color:var(--navy);font-weight:700}
.topbar .products{left:514px;top:9px;color:var(--navy);font-weight:700}
.topbar .login{left:580px;top:8px;color:#666}
.topbar .login span{color:var(--muted)}
.topbar .cartlink{left:709px;top:8px;color:var(--red);font-weight:700}
.brand{left:476px;top:56px;font-size:19px;font-weight:700;color:var(--blue);letter-spacing:.5px;display:flex;align-items:center;gap:10px}
.brand .dot{width:22px;height:22px;border-radius:50%;background:var(--red)}
.brand small{position:absolute;left:14px;top:20px;font-size:11px;font-weight:400;letter-spacing:4px;color:#555;white-space:nowrap}
/* sidebar */
.side{left:210px;top:113px;width:180px;border-top:1px solid var(--navy)}
.side .item{position:absolute;left:0;width:180px;height:27px;border-bottom:1px solid var(--line);font-size:10px;color:#444;padding:8px 0 0 45px}
.side .item svg{position:absolute;left:29px;top:8px}
.side .head{position:absolute;left:24px;top:9px;font-weight:700;color:var(--navy);font-size:10px}
.fruitlist{position:absolute;left:46px;top:104px;border-left:1px solid var(--line);padding-left:10px}
.fruitlist div{height:17px;font-size:8px;color:#666}
/* search */
.search{left:410px;top:114px;width:380px;height:26px;border:1px solid #888;display:flex;font-size:9px}
.search .q{flex:0 0 180px;color:var(--faint);padding:8px 0 0 22px;position:relative}
.search .q svg{position:absolute;left:9px;top:8px}
.search .btn{flex:0 0 46px;background:#505050;color:var(--white);font-weight:700;text-align:center;padding-top:7px;font-size:10px}
.search .sel{flex:1;border-left:1px solid #ccc;color:var(--faint);padding:8px 0 0 10px;position:relative}
.search .sel:after{content:"";position:absolute;right:10px;top:9px;width:4px;height:4px;border-right:1px solid #666;border-bottom:1px solid #666;transform:rotate(45deg)}
.crumb{left:410px;top:150px;font-size:8px;color:var(--faint)}
.crumb span{color:var(--blue)}
/* cards */
.card{position:absolute;width:113px;height:182px;background:var(--white);box-shadow:0 0 3px rgba(0,0,0,.15)}
.card .pic{position:absolute;left:8px;top:8px;width:97px;height:92px;border-radius:40px}
.apple-red{background:radial-gradient(circle at 45% 45%,#e23a3a,#a5121a 70%,#fff 72%)}
.apple-green{background:radial-gradient(circle at 50% 50%,#9be04b,#5fae1f 68%,#fff 70%)}
.orange{background:radial-gradient(circle at 50% 50%,#ffb23a,#f27c0c 68%,#fff 70%)}
.banana{background:radial-gradient(ellipse at 50% 55%,#f7d531,#e2b50c 60%,#fff 70%)}
.berry{background:radial-gradient(circle at 50% 55%,#e7343b,#b51a22 62%,#fff 70%)}
.mango{background:radial-gradient(circle at 50% 50%,#f7c125,#d9682a 45%,#8a9b2d 64%,#fff 70%)}
.card .qty{position:absolute;left:8px;top:114px;width:97px;height:12px;border-bottom:1px solid #eee;font-size:8px;text-align:center;color:#555}
.card .qty b{position:absolute;top:-2px;font-size:11px}
.card .qty .m{left:2px}.card .qty .p{right:2px}
.card .name{position:absolute;left:7px;top:132px;font-size:8px;color:#555}
.card .price{position:absolute;left:7px;top:152px;font-size:11px;font-weight:700;color:var(--blue)}
.card .ea{position:absolute;left:7px;top:167px;font-size:7px;color:var(--faint)}
.card .add{position:absolute;right:7px;top:154px;width:40px;height:20px;background:var(--blue);color:var(--white);font-weight:700;font-size:11px;text-align:center;padding-top:4px}
/* right column */
.collect{left:810px;top:113px;width:180px;height:54px;border:1px solid var(--green);padding:8px 0 0 46px}
.delivery{left:810px;top:167px;width:180px;height:45px;padding:8px 0 0 46px;box-shadow:0 1px 2px rgba(0,0,0,.08)}
.rtitle{font-size:10px;font-weight:700;color:#333;position:relative}
.rtitle svg{position:absolute;left:-14px;top:0}
.rsub{font-size:7px;color:#555;margin-top:6px;line-height:11px}
.cart{left:810px;top:232px;width:180px;height:160px;border:1px solid var(--red)}
.cart .t{position:absolute;left:46px;top:8px;font-size:10px;font-weight:700;color:var(--red)}
.cart .t svg{position:absolute;left:-14px;top:0}
.cart .sub{position:absolute;left:46px;top:25px;font-size:8px;color:var(--blue)}
.cart .total{position:absolute;left:46px;top:36px;font-size:19px;font-weight:700;color:var(--blue)}
.cart .checkout{position:absolute;left:46px;top:64px;width:111px;height:27px;background:var(--red);color:var(--white);font-weight:700;font-size:11px;text-align:center;padding-top:8px}
.cart .count{position:absolute;left:46px;top:104px;font-size:8px;color:#555}
.cart .row{position:absolute;left:0;width:178px;height:20px;border-top:1px solid #eee;font-size:8px;color:#444;padding-top:6px}
.cart .row .amt{position:absolute;left:7px;color:var(--blue);font-weight:700}
.cart .row .desc{position:absolute;left:46px}
.cart .row .rm{position:absolute;right:7px;top:6px;width:7px;height:7px;border-radius:50%;background:#444}
.cart .row .rm:after{content:"";position:absolute;left:2px;top:3px;width:3px;height:1px;background:var(--white)}
/* footer */
.footer{left:210px;top:1005px;width:780px;height:194px;background:var(--foot)}
.footer h4{position:absolute;font-size:9px;font-weight:700;color:#333}
.appbadge{left:24px;top:48px;width:110px;height:32px;border-radius:4px;background:#111}
.links{position:absolute;font-size:9px;color:#444;line-height:20px}
.social{position:absolute;top:29px;width:47px;height:47px}
.fb{left:600px;background:#3b5598}.tw{left:655px;background:#1ca7e1}.yt{left:710px;background:#d7262c}
.paycard{position:absolute;top:148px;width:24px;height:15px;border-radius:2px;background:#555}
.secure{left:97px;top:146px;width:16px;height:16px;border-radius:50%;background:#f4b400}
.footer .note{position:absolute;font-size:9px;color:#444}
</style>
</head>
<body>
<div class="abs scene-left" role="img" aria-label="Food photography: pasta bowl, pizza and plated meal"></div>
<div class="abs scene-right" role="img" aria-label="Food photography: salad, strawberry tart and fruit salad"></div>
<div class="abs page"></div>

<header class="abs topbar">
  <div class="abs phone">
    <svg width="9" height="9" viewBox="0 0 10 10" style="vertical-align:-1px;margin-right:3px"><path d="M2 0l2 2.5-1.2 1.3a6 6 0 003.4 3.4L7.5 6 10 8 8.5 10C4 9.5.5 6 0 1.5z" fill="#1b4f9c"/></svg>1300 555 019</div>
  <div class="abs products">Products</div>
  <div class="abs login"><svg width="8" height="9" viewBox="0 0 8 9" style="vertical-align:-1px;margin-right:4px"><circle cx="4" cy="2.3" r="2.2" fill="#777"/><path d="M0 9c0-3 1.8-4.5 4-4.5S8 6 8 9z" fill="#777"/></svg>Login <span>or</span> Register</div>
  <div class="abs cartlink"><svg width="10" height="9" viewBox="0 0 10 9" style="vertical-align:-1px;margin-right:3px"><path d="M0 0h2l.4 1.5H10L9 5.5H3.2L3.5 6.5H9v1H2.8L1.4 1H0z" fill="#e8202a"/><circle cx="3.5" cy="8.3" r=".7" fill="#e8202a"/><circle cx="8" cy="8.3" r=".7" fill="#e8202a"/></svg>My Cart</div>
</header>

<div class="abs brand">BROVAN MARKET<span class="dot"></span><small>SUPERMARKETS</small></div>

<nav class="abs side">
  <div class="head">Category</div>
  <div class="item" style="top:27px;border-bottom:1px solid #f4c242"><svg width="10" height="10" viewBox="0 0 10 10"><path d="M5 0l1.5 3.2 3.5.4-2.6 2.4.7 3.5L5 7.8 1.9 9.5l.7-3.5L0 3.6l3.5-.4z" fill="#f4a51c"/></svg>Favorites</div>
  <div class="item" style="top:54px;border-bottom:1px solid var(--red)"><svg width="10" height="10" viewBox="0 0 10 10"><text x="2" y="9" font-size="10" font-weight="700" fill="#e8202a" font-family="Arimo,sans-serif">$</text></svg>Online Specials</div>
  <div class="item" style="top:81px;border:0;color:var(--blue);font-weight:700"><svg width="9" height="9" viewBox="0 0 9 9"><rect x=".5" y=".5" width="8" height="8" rx="1.5" fill="none" stroke="#1565b4"/><path d="M2.5 4.5h4" stroke="#1565b4"/></svg>Fruit<span style="position:absolute;right:0;top:7px;font-weight:400">›</span></div>
  <div class="fruitlist">
    <div>Apples</div><div>Appricots</div><div>Avocados</div><div>Bananas</div><div>Berries</div><div>Citrus</div><div>Dates</div><div>Grapes</div><div>Melons</div><div>Peaches</div><div>Pear</div>
  </div>
  <div style="position:absolute;top:295px;left:0;width:180px;border-top:1px solid var(--navy)"></div>
  <div class="item" style="top:296px">Vegetables</div>
  <div class="item" style="top:323px">Meat</div>
  <div class="item" style="top:350px">Serviced Deli</div>
  <div class="item" style="top:377px">Bakery</div>
  <div class="item" style="top:404px">Chilled Foods</div>
  <div class="item" style="top:431px">Frozen Foods</div>
  <div class="item" style="top:458px">Milk</div>
  <div class="item" style="top:485px;border:0">Baby</div>
</nav>
<style>
.side .item:nth-of-type(n+5)::before{content:"";position:absolute;left:29px;top:9px;width:8px;height:8px;border:1px solid #888;border-radius:2px;background:linear-gradient(#888,#888) center/4px 1px no-repeat,linear-gradient(#888,#888) center/1px 4px no-repeat}
</style>

<div class="abs search">
  <div class="q"><svg width="9" height="9" viewBox="0 0 9 9"><circle cx="3.6" cy="3.6" r="2.8" fill="none" stroke="#333" stroke-width="1.2"/><path d="M5.6 5.6L8.5 8.5" stroke="#333" stroke-width="1.3"/></svg>Search Product, category, or brand</div>
  <div class="btn">Search</div>
  <div class="sel">Filter by</div>
  <div class="sel">Sort by</div>
</div>
<div class="abs crumb"><span>Home</span> › Fruit</div>

<main>
  <div class="card" style="left:410px;top:167px"><div class="pic apple-red" role="img" aria-label="Red apples"></div><div class="qty"><b class="m">−</b>1<b class="p">+</b></div><div class="name">Apples Red 2Kg Bag</div><div class="price">$8.39</div><div class="ea">$8.39 ea</div><div class="add">ADD</div></div>
  <div class="card" style="left:543px;top:167px"><div class="pic apple-green" role="img" aria-label="Green apple"></div><div class="qty"><b class="m">−</b>1<b class="p">+</b></div><div class="name">Green Apples Each</div><div class="price">$0.60</div><div class="ea">$0.60 ea</div><div class="add">ADD</div></div>
  <div class="card" style="left:677px;top:167px"><div class="pic orange" role="img" aria-label="Orange with slice"></div><div class="qty"><b class="m">−</b>1<b class="p">+</b></div><div class="name">Oranges Each</div><div class="price">$0.80</div><div class="ea">$0.80 ea</div><div class="add">ADD</div></div>

  <div class="card" style="left:410px;top:369px"><div class="pic banana" role="img" aria-label="Bunch of bananas"></div><div class="qty"><b class="m">−</b>1<b class="p">+</b></div><div class="name">Banana 1Kg Bag</div><div class="price">$4.49</div><div class="ea">$4.49 ea</div><div class="add">ADD</div></div>
  <div class="card" style="left:543px;top:369px"><div class="pic berry" role="img" aria-label="Strawberries"></div><div class="qty"><b class="m">−</b>1<b class="p">+</b></div><div class="name">Strawberry 1 Pack</div><div class="price">$5.00</div><div class="ea">$5.00 ea</div><div class="add">ADD</div></div>
  <div class="card" style="left:677px;top:369px"><div class="pic mango" role="img" aria-label="Mango cut and whole"></div><div class="qty"><b class="m">−</b>1<b class="p">+</b></div><div class="name">Mango Each</div><div class="price">$4.20</div><div class="ea">$4.20 ea</div><div class="add">ADD</div></div>

  <div class="card" style="left:410px;top:572px"><div class="pic apple-red" role="img" aria-label="Red apples"></div><div class="qty"><b class="m">−</b>1<b class="p">+</b></div><div class="name">Apples Red 2Kg Bag</div><div class="price">$8.39</div><div class="ea">$8.39 ea</div><div class="add">ADD</div></div>
  <div class="card" style="left:543px;top:572px"><div class="pic apple-green" role="img" aria-label="Green apple"></div><div class="qty"><b class="m">−</b>1<b class="p">+</b></div><div class="name">Green Apples Each</div><div class="price">$0.60</div><div class="ea">$0.60 ea</div><div class="add">ADD</div></div>
  <div class="card" style="left:677px;top:572px"><div class="pic orange" role="img" aria-label="Orange with slice"></div><div class="qty"><b class="m">−</b>1<b class="p">+</b></div><div class="name">Oranges Each</div><div class="price">$0.80</div><div class="ea">$0.80 ea</div><div class="add">ADD</div></div>

  <div class="card" style="left:410px;top:774px"><div class="pic banana" role="img" aria-label="Bunch of bananas"></div><div class="qty"><b class="m">−</b>1<b class="p">+</b></div><div class="name">Banana 1Kg Bag</div><div class="price">$4.49</div><div class="ea">$4.49 ea</div><div class="add">ADD</div></div>
  <div class="card" style="left:543px;top:774px"><div class="pic berry" role="img" aria-label="Strawberries"></div><div class="qty"><b class="m">−</b>1<b class="p">+</b></div><div class="name">Strawberry 1 Pack</div><div class="price">$5.00</div><div class="ea">$5.00 ea</div><div class="add">ADD</div></div>
</main>

<aside>
  <div class="abs collect"><div class="rtitle"><svg width="9" height="9" viewBox="0 0 9 9"><path d="M0 1h9v2H0zM1 3h7v6H1z" fill="#8cc63f"/></svg>Click and Collect</div><div class="rsub">12 Harbour Lane Brovan<br>TAS 7000</div></div>
  <div class="abs delivery"><div class="rtitle"><svg width="11" height="9" viewBox="0 0 11 9"><path d="M0 1h7v6H0zM7 3h2.5L11 5v2H7z" fill="#444"/><circle cx="2.5" cy="7.8" r="1.1" fill="#444"/><circle cx="9" cy="7.8" r="1.1" fill="#444"/></svg>Delivery</div><div class="rsub">Currently not available</div></div>

  <div class="abs cart">
    <div class="t"><svg width="10" height="9" viewBox="0 0 10 9"><path d="M0 0h2l.4 1.5H10L9 5.5H3.2L3.5 6.5H9v1H2.8L1.4 1H0z" fill="#e8202a"/><circle cx="3.5" cy="8.3" r=".7" fill="#e8202a"/><circle cx="8" cy="8.3" r=".7" fill="#e8202a"/></svg>My Cart</div>
    <div class="sub">Sub Totals</div>
    <div class="total">$44.56</div>
    <div class="checkout">CHECKOUT</div>
    <div class="count">Total 6 Items</div>
    <div class="row" style="top:119px"><span class="amt">$33.56</span><span class="desc">4 x Apples Red 2kg Bag</span><span class="rm"></span></div>
    <div class="row" style="top:139px"><span class="amt">$10.00</span><span class="desc">2 x Strawberry 1 Pack</span><span class="rm"></span></div>
  </div>
</aside>

<footer class="abs footer">
  <h4 style="left:22px;top:28px">Download Our App</h4>
  <div class="abs appbadge" aria-label="App store badge"></div>
  <div class="links" style="left:200px;top:22px">My Account<br>My Past Order<br>Online Specials<br>Everyday Specials</div>
  <div class="links" style="left:333px;top:22px">Delivery<br>FAQ<br>Privacy Policy<br>Terms and Conditions</div>
  <div class="links" style="left:467px;top:27px;line-height:11px">End User License<br>Agreement</div>
  <div class="social fb" aria-label="Social link"></div>
  <div class="social tw" aria-label="Social link"></div>
  <div class="social yt" aria-label="Social link"></div>
  <h4 style="left:22px;top:128px">We Accept</h4>
  <div class="paycard" style="left:22px" aria-label="Payment card"></div>
  <div class="paycard" style="left:59px" aria-label="Payment card"></div>
  <div class="abs secure"></div>
  <div class="note" style="left:118px;top:150px">100% Secure</div>
  <div class="note" style="right:22px;top:150px">© Qline Pty Ltd 2014 - All Rights Reserved ver 1.1.6</div>
</footer>
</body>
</html>
```